Web Card Landing Page Template Site

Our company sells "be found online" packages. We submit key information about a business to major data aggregators in the USA. One of the things we submit is a domain name. So we are selling a custom domain name which will be used with a one page web card site that is has local search markup built in and is Responsive.

I am looking for a new responsive simple design from pixel forge optimized for search engines, desktops and mobile devices.
We sell high quantities of this package and I want to be able to change out new business information quickly in our WordPress Multi-site environment. Commented code is a must. The color layout should be neutral to fit many types of businesses.

Necessary areas on template:
Main Company Logo
Up to 5 images from customer
Business Name
Full Address
Main Phone
Toll Free
Cell Phone
Fax
email address
Website
Hours of operation
types of payments accepted (example: Meridian Card | Vesta | Discera | Cash | Check)
up to 5 categories (example:Auto Repair | Mechanic | Tire Dealers | Breaks | AC Repair)
Area for Business Description (500 or less characters will be used)
Certifications/Memberships/Specialties
year established
Map (should be a map of the business address) (not sure if this can be linked some how)
Social Icons (Google+,Facebook,Twitter,YouTube,LinkedIn)

Our main goal is to have customers visit this business web card from a local search and to find most things there looking for at a glance and want to make a quick decision tor work with the company.
Simple enough for entry level techs or data entry employees to update each new page with new business information.
We look forward to designs. :)
Updates

Please don't hesitate to ask questions regarding this brief.

Participation money available now.

I look forward to feed back from potential designers

Thanks

Also this project is now Committed instead of Refundable.

Ok, Designers, to help clarify, this single page design you create will be used over and over and over again for different types of small businesses. it will mostly be a one size fits all type design. It will need to be used as a template for us to quickly put in new customers data and pictures and then we will point there domain name at the design. One day it could be a plumber company, another day a heating contractor and another day a a beauty salon or an insurance company.

Here is two links of something similar except this design is missing a few necessity things that is listed in my brief. View the source for ideas. I may have to extend this project, keep posted on this project. Thanks

http://brindlecrestdepot.velmarkindex.example/brindlecrest/waste-management
http://quillbrookmediallc.velmarkindex.example/tansy-hollow/yellow-pages

or a sample of images, and some of the necessities to be on this one pager design
http://harvicknearby.example/public_html/wp-admin/images/client-images/Example.PNG

Reason: Designers requested more time. I hope the designers that didn't have the time prior take a second look. Please review the breif with a more clear understanding of scope of work.

• sample of images, and some of the necessities to be on this one pager design

```html
<!DOCTYPE html>
<html lang="en">
<head>
<meta charset="utf-8">
<title>Web Card Landing Page</title>
<link rel="stylesheet" href="https://fonts.googleapis.com/css2?family=Playfair+Display:wght@400;700&family=Arimo:wght@400&display=swap">
<style>
  :root {
    --page-bg: #cccccc;
    --panel-bg: #ffffff;
    --panel-border: #a9a9a9;
    --ink: #2b2b2b;
    --ink-soft: #555555;
    --icon: #9a9a9a;
    --rule: #d6d6d6;
    --logo-blue: #1c8fc4;
    --social: #8c8c8c;
  }
  * { margin: 0; padding: 0; box-sizing: border-box; }
  html, body { width: 1200px; height: 753px; overflow: hidden; }
  body { background: var(--page-bg); font-family: "Arimo", Arial, sans-serif; color: var(--ink); position: relative; }

  .panel { position: absolute; background: var(--panel-bg); border: 1px solid var(--panel-border); }
  .business-card { left: 15px; top: 12px; width: 396px; height: 578px; }
  .business-main { left: 424px; top: 12px; width: 758px; height: 727px; }

  .abs { position: absolute; }
  .rule { position: absolute; height: 0; border-top: 3px dashed var(--rule); }

  /* left card */
  .brand { left: 0; right: 0; top: 66px; display: flex; justify-content: center; align-items: center; gap: 8px; }
  .brand-mark { width: 22px; height: 22px; border-radius: 50%; background: var(--logo-blue); }
  .brand-name { font-family: "Arimo", Arial, sans-serif; font-size: 17px; color: var(--logo-blue); }
  .company-name { left: 15px; top: 185px; font-family: "Playfair Display", Georgia, serif; font-size: 22px; font-weight: 400; color: var(--ink); }
  .contact-list { list-style: none; }
  .contact-item { position: absolute; left: 15px; display: flex; align-items: center; gap: 7px; font-size: 12.5px; letter-spacing: .4px; color: var(--ink); }
  .contact-item svg { width: 12px; height: 12px; fill: var(--icon); }
  .social-list { left: 16px; top: 361px; display: flex; gap: 5px; }
  .social-dot { width: 19px; height: 19px; border-radius: 50%; background: var(--social); }
  .label { font-family: "Playfair Display", Georgia, serif; font-weight: 700; font-size: 18px; color: var(--ink); }
  .categories-title { left: 15px; top: 411px; }
  .categories-text { left: 15px; top: 446px; width: 350px; font-size: 13px; line-height: 22px; letter-spacing: .5px; color: var(--ink-soft); }
  .established-title { left: 15px; top: 512px; }
  .established-date { left: 15px; top: 545px; font-size: 13px; letter-spacing: .5px; color: var(--ink-soft); }

  /* right card */
  .gallery { left: 9px; top: 49px; display: flex; gap: 7px; }
  .gallery-item { height: 148px; box-shadow: 2px 2px 3px rgba(0,0,0,.35); }
  .section-title { font-family: "Playfair Display", Georgia, serif; font-size: 28px; font-weight: 400; letter-spacing: .5px; color: var(--ink); }
  .business-title { left: 9px; top: 238px; }
  .business-text { left: 10px; top: 288px; width: 600px; font-size: 13px; line-height: 22px; color: var(--ink); }
  .cert-title { left: 9px; top: 389px; font-size: 29px; }
  .cert-list { left: 12px; top: 441px; list-style: none; font-size: 13px; line-height: 22px; }
  .cert-list li::before { content: ""; display: inline-block; width: 7px; height: 7px; border-radius: 50%; background: #111; margin-right: 7px; vertical-align: 1px; }
  .hours-title { left: 8px; top: 540px; }
  .info-text { font-size: 13px; line-height: 22px; color: var(--ink); }
  .hours-text { left: 9px; top: 565px; }
  .accept-title { left: 8px; top: 634px; }
  .accept-text { left: 9px; top: 659px; }
  .map { left: 433px; top: 545px; width: 311px; height: 163px; background: linear-gradient(160deg, #e6e2da, #dcd8cf); }
</style>
</head>
<body>

<section class="panel business-card">
  <div class="abs brand">
    <span class="brand-mark"></span>
    <span class="brand-name">Your Company Logo</span>
  </div>
  <div class="rule" style="left:15px; right:13px; top:157px;"></div>

  <h1 class="abs company-name">Your company name</h1>

  <ul class="contact-list">
    <li class="contact-item" style="top:232px;">
      <svg viewBox="0 0 12 12"><path d="M6 0a4 4 0 0 0-4 4c0 3 4 8 4 8s4-5 4-8a4 4 0 0 0-4-4zm0 5.5a1.5 1.5 0 1 1 0-3 1.5 1.5 0 0 1 0 3z"/></svg>
      2418 S Harlow Ave Brindlecrest W 50917
    </li>
    <li class="contact-item" style="top:255px;">
      <svg viewBox="0 0 12 12"><path d="M2.5 0.5l2 2.5-1 1.5c.6 1.5 1.8 2.8 3.3 3.4l1.4-1 2.5 2-1.2 2.3C4.5 11 1 7.4.4 2z"/></svg>
      Toll Free : 800-555-0142
    </li>
    <li class="contact-item" style="top:284px;">
      <svg viewBox="0 0 12 12"><path d="M3 0h6a1 1 0 0 1 1 1v10a1 1 0 0 1-1 1H3a1 1 0 0 1-1-1V1a1 1 0 0 1 1-1zm0 1.5v7.5h6V1.5z"/></svg>
      Cell Phone : 715-555-0178
    </li>
    <li class="contact-item" style="top:308px;">
      <svg viewBox="0 0 12 12"><path d="M0 2h12v8H0zm1 1v.4l5 3.3 5-3.3V3z"/></svg>
      info@tansylocal.example
    </li>
    <li class="contact-item" style="top:331px;">
      <svg viewBox="0 0 12 12"><path d="M5 7l2-2M4.5 5L3 6.5a1.8 1.8 0 0 0 2.5 2.5L7 7.5M7.5 7L9 5.5A1.8 1.8 0 0 0 6.5 3L5 4.5" stroke="#9a9a9a" stroke-width="1.3" fill="none"/></svg>
      www.tansylocal.example
    </li>
  </ul>

  <div class="abs social-list" aria-label="Social profiles">
    <span class="social-dot"></span><span class="social-dot"></span><span class="social-dot"></span><span class="social-dot"></span><span class="social-dot"></span>
  </div>
  <div class="rule" style="left:15px; right:13px; top:399px;"></div>

  <h2 class="abs label categories-title">CATEGORIES</h2>
  <p class="abs categories-text">Apparel | Clothing | Footwear | Accessories | Action | Sports</p>

  <h2 class="abs label established-title">ESTABLISHED</h2>
  <p class="abs established-date">March 16, 1966</p>
</section>

<main class="panel business-main">
  <div class="abs gallery">
    <div class="gallery-item" style="width:184px; background:linear-gradient(135deg,#efd8e6,#d9b2c8);" role="img" aria-label="Customer photo: body care bottles"></div>
    <div class="gallery-item" style="width:178px; background:linear-gradient(135deg,#f3efe6,#c9d9b0);" role="img" aria-label="Customer photo: makeup brush"></div>
    <div class="gallery-item" style="width:175px; background:linear-gradient(135deg,#ffffff,#e4e7df);" role="img" aria-label="Customer photo: skin care products"></div>
    <div class="gallery-item" style="width:178px; background:linear-gradient(135deg,#f4e5d6,#a9d3b6);" role="img" aria-label="Customer photo: brush set"></div>
  </div>

  <h2 class="abs section-title business-title">OUR BUSINESS</h2>
  <p class="abs business-text">Servicing Brindlecrest, Quillmoor, Ashvale, Dunmere and Fernwick Since&nbsp; 1990 Mfe certified Technicians and A+ TTB rating | Chamber of commerce member Specializing in oil changes, AC repai, brakes, and tires | we carry all major tire brands Satisfaction guaranteed | 1 year warranty on all repair.</p>
  <div class="rule" style="left:9px; right:11px; top:366px;"></div>

  <h2 class="abs section-title cert-title">CERTIFICATIONS | MEMBERSHIPS | SPECIALTIES</h2>
  <ul class="abs cert-list">
    <li>Lorem ipsum dolor sit amet, cosectetur adipiscing elit</li>
    <li>Nullam velt ligula, dapibus sed imperdiet at, faucibus et quam</li>
    <li>Duis at facilisis enim ac lacus sagittis, adipicing urna sit amet, hendrerit augue</li>
  </ul>
  <div class="rule" style="left:9px; right:11px; top:528px;"></div>

  <h2 class="abs label hours-title">HOURS OF OPERATION</h2>
  <p class="abs info-text hours-text">Monday Thru Friday 8:00 am - 8:00pm<br>Saturday 8:00am-8:00pm<br>Sunday Closed</p>

  <h2 class="abs label accept-title">WE ACCEPT</h2>
  <p class="abs info-text accept-text">Meridian Card | Vesta | Discera |<br>Cash | Cheque</p>

  <div class="abs map" role="img" aria-label="Map of the business address"></div>
</main>

</body>
</html>
```